Obrelo Business Card

Need a double sided business card. Would like the business card to have the logo on one side and the employees details and business contact details on the other.

Business

```html
<!DOCTYPE html>
<html lang="en">
<head>
<meta charset="utf-8">
<title>Obrelo Business Card</title>
<link rel="stylesheet" href="https://fonts.googleapis.com/css2?family=Source+Sans+3:wght@400;600;700&display=swap">
<style>
  :root {
    --backdrop: #e9e6e1;
    --card-black: #000000;
    --brand-green: #a4ce4a;
    --ink-dark: #333333;
    --ink-white: #ffffff;
    --edge-light: #f2f2f2;
  }
  * { box-sizing: border-box; margin: 0; padding: 0; }
  html, body {
    width: 1200px;
    height: 813px;
    overflow: hidden;
    background: var(--backdrop);
    font-family: "Source Sans 3", sans-serif;
  }
  .canvas {
    position: relative;
    width: 1200px;
    height: 813px;
  }
  .card {
    position: absolute;
    width: 520px;
    height: 310px;
    border-radius: 22px;
    overflow: hidden;
  }
  .card--details {
    left: 320px;
    top: 50px;
    background: var(--card-black);
    border: 2px solid var(--edge-light);
    border-radius: 14px;
  }
  .card--logo-dark {
    left: 70px;
    top: 440px;
    background: var(--card-black);
  }
  .card--logo-light {
    left: 610px;
    top: 440px;
    background: var(--brand-green);
  }
  .wordmark {
    position: absolute;
    font-weight: 700;
    letter-spacing: 1px;
    line-height: 1;
  }
  .card--details .wordmark {
    left: 54px;
    top: 178px;
    font-size: 58px;
    color: var(--brand-green);
  }
  .card--logo-dark .wordmark {
    left: 0;
    right: 0;
    top: 104px;
    text-align: center;
    font-size: 96px;
    color: var(--brand-green);
  }
  .card--logo-light .wordmark {
    left: 0;
    right: 0;
    top: 78px;
    text-align: center;
    font-size: 96px;
    color: var(--ink-white);
  }
  .web-address {
    position: absolute;
    left: 0;
    right: 0;
    top: 214px;
    text-align: center;
    font-size: 17px;
    font-weight: 600;
    letter-spacing: 2px;
    color: var(--card-black);
  }
  .details-panel {
    position: absolute;
    left: 266px;
    top: 18px;
    width: 236px;
    height: 268px;
    background: var(--brand-green);
    border-radius: 26px;
    padding: 22px 24px;
    color: var(--ink-dark);
  }
  .person-name {
    font-size: 19px;
    font-weight: 700;
    line-height: 1.1;
  }
  .person-title {
    font-size: 16px;
    margin-top: 4px;
  }
  .contact-list {
    list-style: none;
    margin-top: 18px;
  }
  .contact-item {
    display: flex;
    align-items: center;
    gap: 5px;
    font-size: 16px;
    line-height: 1.45;
  }
  .contact-item--email { font-size: 14px; }
  .contact-icon {
    width: 12px;
    height: 12px;
    fill: var(--ink-dark);
    flex: none;
  }
  .address {
    font-style: normal;
    font-size: 14px;
    line-height: 1.35;
    margin-top: 20px;
  }
</style>
</head>
<body>
<main class="canvas">

  <section class="card card--details" aria-label="Business card, details side">
    <span class="wordmark">obrelo</span>
    <div class="details-panel">
      <p class="person-name">Your Name</p>
      <p class="person-title">Title</p>
      <ul class="contact-list">
        <li class="contact-item">
          <svg class="contact-icon" viewBox="0 0 24 24" aria-hidden="true"><path d="M6.6 10.8a15.1 15.1 0 0 0 6.6 6.6l2.2-2.2c.3-.3.7-.4 1-.2 1.1.4 2.3.6 3.6.6.6 0 1 .4 1 1V20c0 .6-.4 1-1 1A17 17 0 0 1 3 4c0-.6.4-1 1-1h3.5c.6 0 1 .4 1 1 0 1.3.2 2.5.6 3.6.1.3 0 .7-.2 1z"/></svg>
          123-456-7980
        </li>
        <li class="contact-item">
          <svg class="contact-icon" viewBox="0 0 24 24" aria-hidden="true"><rect x="6" y="1" width="12" height="22" rx="2"/></svg>
          123-568-7896
        </li>
        <li class="contact-item contact-item--email">
          <svg class="contact-icon" viewBox="0 0 24 24" aria-hidden="true"><path d="M2 5h20v14H2z M2 5l10 8 10-8" stroke="#a4ce4a" stroke-width="2"/></svg>
          hello@obrelo.com
        </li>
      </ul>
      <address class="address">Street Name, City Name<br>State ZipCode</address>
    </div>
  </section>

  <section class="card card--logo-dark" aria-label="Business card, logo side on black">
    <span class="wordmark">obrelo</span>
  </section>

  <section class="card card--logo-light" aria-label="Business card, logo side on green">
    <span class="wordmark">obrelo</span>
    <p class="web-address">www.obrelo.com</p>
  </section>

</main>
</body>
</html>
```